COVID-19 Accredited CME Impact Infographic

We want an infographic showing how much COVID-19 Continuing Medical Education we have accredited and its impact. Our website is at https://med.halvering.edu/cme/COVID19/education.html The attached document is intended to simply show the elements. You have complete freedom on design. We will be updating the numbers weekly so it is important that we have the files so that we can update it. This can be done in powerpoint, publisher, word, in-design, illustrator. Don't use crazy fonts that we wont have.

Target Market(s)

Internal to Halvering. We just want to show the impact of our work

Industry/Entity Type

Education

Requirements
Must have
• We must be able to update the numbers ourselves.

See attached document for the pieces that we want.

The sizes of the numbers in the attached are based on importance to us.
Nice to have
• Not mandatory but try to use these colors. https://med.halvering.edu/identity/color-palette.html

I was thinking that perhaps the big number could be done in traditional train. Like this: https://www.pictovane.com/image-illustration/flip-board-under-constuction-page-isolated-8803617452

```html
<!DOCTYPE html>
<html lang="en">
<head>
<meta charset="utf-8">
<title>COVID-19 CME Impact</title>
<link rel="stylesheet" href="https://fonts.googleapis.com/css2?family=Barlow:wght@400;700;800&family=Barlow+Semi+Condensed:wght@600;700&family=Source+Serif+4:wght@500&display=swap">
<style>
  :root {
    --cardinal: #8c1515;
    --cardinal-deep: #6e0f13;
    --cardinal-soft: #b04a4e;
    --paper: #ffffff;
    --footer: #333333;
    --footer-text: #f2f2f2;
  }
  html, body { margin: 0; padding: 0; overflow: hidden; background: var(--paper); }
  .canvas {
    position: relative;
    width: 1200px;
    height: 1155px;
    overflow: hidden;
    background: var(--paper);
    font-family: "Barlow Semi Condensed", "Barlow", sans-serif;
    color: var(--cardinal);
  }

  /* Header band */
  .header-band {
    position: absolute; left: 0; top: 0; width: 1200px; height: 288px;
    background: var(--cardinal);
  }
  .brand-plate {
    position: absolute; left: 60px; top: 99px; width: 245px; height: 95px;
    background: var(--paper);
    display: flex; align-items: center; justify-content: center;
  }
  .brand-name {
    font-family: "Barlow", sans-serif; font-weight: 700;
    font-size: 26px; letter-spacing: 0.5px; color: var(--cardinal);
    line-height: 1.1; text-align: center;
  }
  .headline {
    position: absolute; left: 366px; top: 78px; margin: 0;
    font-family: "Barlow", sans-serif; font-weight: 700;
    font-size: 122px; line-height: 1; color: var(--paper);
    letter-spacing: 1px; white-space: nowrap;
  }

  /* Stat boxes */
  .stat {
    position: absolute; box-sizing: border-box;
    border: 3px solid var(--cardinal); border-radius: 12px;
    display: flex; align-items: center; justify-content: center;
  }
  .stat-label {
    position: absolute; left: 50%; top: 0;
    transform: translate(-50%, -55%);
    background: var(--paper); padding: 0 16px;
    font-weight: 700; font-size: 22px; white-space: nowrap; line-height: 1;
  }
  .stat-value {
    font-family: "Barlow", sans-serif; font-weight: 700;
    font-size: 76px; line-height: 1; margin-top: 6px; letter-spacing: -1px;
  }
  .stat--states    { left: 64px;  top: 373px; width: 229px; height: 97px; }
  .stat--countries { left: 331px; top: 373px; width: 226px; height: 97px; }
  .stat--cme       { left: 65px;  top: 517px; width: 493px; height: 109px; }
  .stat--live      { left: 65px;  top: 677px; width: 493px; height: 109px; }
  .stat--views     { left: 62px;  top: 859px; width: 1075px; height: 168px; }
  .stat--views .stat-label { font-size: 34px; padding: 0 20px; }
  .stat--views .stat-value { font-size: 116px; margin-top: 10px; }

  .stat--activities {
    left: 634px; top: 371px; width: 503px; height: 415px;
    display: block;
  }
  .stat--activities .stat-label { font-size: 35px; padding: 0 20px; }

  /* Flip board */
  .flip-card {
    position: absolute; top: 74px; width: 202px; height: 286px;
    box-sizing: border-box;
    border: 11px solid var(--cardinal); border-radius: 24px;
    background: var(--paper);
    display: flex; align-items: center; justify-content: center;
  }
  .flip-card--tens { left: 32px; }
  .flip-card--ones { left: 265px; }
  .flip-digit {
    font-family: "Barlow", sans-serif; font-weight: 700;
    font-size: 250px; line-height: 1; margin-top: 8px;
  }
  .flip-seam {
    position: absolute; left: 0; right: 0; top: 50%; height: 3px;
    background: var(--cardinal); transform: translateY(-50%);
  }
  .flip-hinge {
    position: absolute; top: 50%; width: 18px; height: 46px;
    transform: translateY(-50%);
    background: linear-gradient(to bottom, var(--cardinal-soft) 0 30%, var(--cardinal) 30% 70%, var(--cardinal-deep) 70% 100%);
  }
  .flip-hinge--left  { left: -13px; }
  .flip-hinge--right { right: -13px; }

  /* Footer band */
  .footer-band {
    position: absolute; left: 0; top: 1088px; width: 1200px; height: 67px;
    background: var(--footer); color: var(--footer-text);
    font-family: "Barlow", sans-serif; font-weight: 400; font-size: 18px;
  }
  .footer-date { position: absolute; left: 99px; top: 22px; }
  .footer-url  { position: absolute; right: 102px; top: 22px; }
</style>
</head>
<body>
<main class="canvas">
  <header class="header-band">
    <div class="brand-plate"><span class="brand-name">Halvering Medicine</span></div>
    <h1 class="headline">COVID-19 CME</h1>
  </header>

  <section class="stat stat--states">
    <span class="stat-label"># OF STATES</span>
    <span class="stat-value">26</span>
  </section>

  <section class="stat stat--countries">
    <span class="stat-label"># OF COUNTRIES</span>
    <span class="stat-value">12</span>
  </section>

  <section class="stat stat--cme">
    <span class="stat-label"># OF CME LEARNERS</span>
    <span class="stat-value">5,879</span>
  </section>

  <section class="stat stat--live">
    <span class="stat-label"># OF LIVE LEARNERS</span>
    <span class="stat-value">23,098</span>
  </section>

  <section class="stat stat--activities">
    <span class="stat-label"># OF ACTIVITIES</span>
    <div class="flip-card flip-card--tens">
      <span class="flip-digit">2</span>
      <span class="flip-seam"></span>
      <span class="flip-hinge flip-hinge--left"></span>
      <span class="flip-hinge flip-hinge--right"></span>
    </div>
    <div class="flip-card flip-card--ones">
      <span class="flip-digit">3</span>
      <span class="flip-seam"></span>
      <span class="flip-hinge flip-hinge--left"></span>
      <span class="flip-hinge flip-hinge--right"></span>
    </div>
  </section>

  <section class="stat stat--views">
    <span class="stat-label"># OF TOTAL ON-DEMAND VIEWS</span>
    <span class="stat-value">1,209,987</span>
  </section>

  <footer class="footer-band">
    <span class="footer-date">Current as of 04/10/20</span>
    <span class="footer-url">https://med.halvering.edu/cme/COVID19/education.html</span>
  </footer>
</main>
</body>
</html>
```